Brenmoss Building Company needs a flyer to catch attention

A flyer that can be displayed at several different stores detailing our skills, work produced, experience and contact details. Information can be extracted from our website www.brenmossbc.co.nz. The flyer should feel very green, with addition of pics of work completed as well as stock images of lush green plants, lawns, landscape or similar. Needs to be eye catching with just enough information to express our experience and commitment to high standards

Target Market(s)

Residential
Landscape Architects

Industry/Entity Type

Landscaping

Font styles to use
Serif

Colors
abd037

Requirements
Must have
• Our logo
Experience
Services offered including pictures
All information avail on our website www.brenmossbc.co.nz
Nice to have
• stock images of lush greenery like a garden after fresh rainfall
Should not have
• Nothing comes to mind

```html
<!DOCTYPE html>
<html lang="en">
<head>
<meta charset="utf-8">
<title>Brenmoss Building Company – Landscaping Flyer</title>
<link href="https://fonts.googleapis.com/css2?family=Poppins:wght@300;400;500;600;700;800&display=swap" rel="stylesheet">
<style>
  :root{
    --lime:#7cc242;
    --lime-bright:#abd037;
    --lime-text:#9ccb3b;
    --forest:#138a36;
    --forest-deep:#0d6b2a;
    --pale:#eef3e4;
    --ink:#1d2a1d;
    --white:#ffffff;
    --backdrop:#e9e9e9;
  }
  *{box-sizing:border-box;margin:0;padding:0}
  html,body{width:810px;height:1200px;overflow:hidden;background:var(--backdrop)}
  body{font-family:"Poppins",sans-serif;color:var(--ink)}
  .sheet{position:relative;width:810px;height:1200px;overflow:hidden}

  .page{position:absolute;top:326px;width:810px;height:1146px;overflow:hidden;
    transform:scale(.4778);transform-origin:0 0;box-shadow:0 6px 18px rgba(0,0,0,.25)}
  .page-front{left:12px;background:var(--pale)}
  .page-back{left:411px;background:var(--forest)}

  /* ---------- shared tick list ---------- */
  .tick-list{list-style:none}
  .tick-list li{position:relative;display:flex;align-items:center;padding-left:27px;font-weight:600;text-transform:uppercase;white-space:nowrap}
  .tick-list li::before{content:"";position:absolute;left:0;top:50%;width:18px;height:18px;margin-top:-9px;border-radius:50%;background:var(--lime)}
  .tick-list li::after{content:"";position:absolute;left:5px;top:50%;width:8px;height:4px;margin-top:-4px;border-left:2px solid var(--white);border-bottom:2px solid var(--white);transform:rotate(-45deg)}

  /* ---------- front ---------- */
  .hero-photo{position:absolute;left:0;top:0;width:810px;height:600px;
    background:linear-gradient(180deg,#f4c766 0%,#e9a74a 14%,#6d5a4a 30%,#3a3b36 48%,#4e4f4a 70%,#5b5b55 100%)}
  .greenery-photo{position:absolute;left:0;top:520px;width:810px;height:626px;
    background:radial-gradient(ellipse at 20% 40%,#cfe3b4 0%,#e3eed3 45%,#f3f1e8 100%)}
  .waves{position:absolute;left:0;top:0}

  .brand{position:absolute;left:28px;top:42px;width:260px;text-align:center}
  .brand-mark{width:132px;height:132px;border-radius:50%;background:var(--lime);border:5px solid var(--white);margin:0 auto 8px}
  .brand-name{font-size:19px;font-weight:500;color:var(--white);line-height:1.15}

  .headline{position:absolute;right:30px;top:234px;text-align:right;color:var(--white)}
  .headline-rule{display:block;width:92px;height:4px;background:var(--lime);margin:0 0 8px auto}
  .headline-line{font-size:33px;font-weight:700;line-height:1.3;letter-spacing:.5px}
  .headline-key{font-size:48px;font-weight:800;color:var(--lime);line-height:1.1}
  .headline-place{font-size:32px;line-height:1.35}
  .headline-place b{font-weight:700}
  .headline-place span{font-weight:300}

  .experience{position:absolute;left:50px;top:428px;width:214px;text-align:center;color:var(--white);line-height:1.05}
  .experience-lead,.experience-tail{font-size:13px;font-weight:600}
  .experience-years{font-size:31px;font-weight:800;margin:2px 0}

  .work-photo{position:absolute;left:65px;width:156px;height:156px;border-radius:50%;border:6px solid var(--forest);box-shadow:0 0 0 3px var(--white) inset}
  .work-photo.timber{top:540px;background:linear-gradient(180deg,#dfe9cf 0%,#dcb87a 55%,#c48f45 100%)}
  .work-photo.lawn{top:708px;background:linear-gradient(160deg,#c9c4b5 0%,#8fb657 45%,#4f8a2c 100%)}
  .work-photo.paving{top:882px;background:linear-gradient(150deg,#9a9c96 0%,#7d7f7a 60%,#6b6d68 100%)}

  .services{position:absolute;left:269px;top:694px;width:512px}
  .services-title{font-size:36px;font-weight:800;color:var(--forest);line-height:1}
  .services-rule{width:58px;height:3px;background:var(--lime);margin:6px 0 10px}
  .services-intro{font-size:12.6px;line-height:1.32;color:#222}

  .service-list{position:absolute;top:860px}
  .service-list li{height:34px;font-size:12px;color:#1e1e1e}
  .col-1{left:271px}
  .col-2{left:425px;border-left:2px solid var(--forest);padding-left:10px}
  .col-3{left:580px;border-left:2px solid var(--forest);padding-left:10px}

  .contact-bar{position:absolute;left:0;top:1072px;width:810px;height:48px;background:var(--lime);display:flex;align-items:center;color:var(--white);font-size:18px;font-weight:500}
  .contact-item{flex:1;display:flex;align-items:center;justify-content:center;gap:10px;height:34px}
  .contact-item + .contact-item{border-left:2px solid var(--white)}

  /* ---------- back ---------- */
  .back-photo{position:absolute;left:0;top:0;width:810px;height:900px;
    background:linear-gradient(180deg,#1d6f31 0%,#21893b 18%,#1f8a3a 60%,#1a7d34 100%)}
  .decking-photo{position:absolute;left:0;top:860px;width:810px;height:286px;
    background:linear-gradient(100deg,#3f8a35 0%,#6f7a6c 30%,#8c8f89 60%,#6d706b 100%)}
  .bench-photo{position:absolute;left:434px;top:1004px;width:376px;height:120px;background:#1e221f;
    clip-path:polygon(6% 0,100% 0,100% 100%,0 100%)}
  .swoosh{position:absolute;left:0;top:0}

  .project-grid{position:absolute;left:38px;top:72px;display:grid;grid-template-columns:178px 178px;grid-auto-rows:178px;gap:8px}
  .project-grid div{border:2px solid rgba(255,255,255,.2)}
  .grid-fence{background:linear-gradient(180deg,#e6e2dc 0%,#a8623a 35%,#7a4a2c 100%)}
  .grid-path{background:linear-gradient(180deg,#4d4a42 0%,#c8c8c2 40%,#5f9b3a 65%,#2d2d28 100%)}
  .grid-bench{background:linear-gradient(160deg,#3b4a3c 0%,#c99a4e 45%,#8c8c86 100%)}
  .grid-pool{background:linear-gradient(180deg,#2f4a3a 0%,#3f6d76 35%,#a7aaa3 65%,#c3c4be 100%)}

  .about{position:absolute;left:461px;top:58px;width:301px;color:var(--white)}
  .about-title{font-size:38px;font-weight:800;color:var(--lime-text);line-height:1.1;margin-bottom:12px}
  .about p{font-size:12px;line-height:16.3px;text-align:justify;hyphens:auto;margin-bottom:14px}
  .about .about-values{color:var(--lime-text);font-weight:700}

  .projects{position:absolute;left:42px;top:458px}
  .projects-title{font-size:38px;font-weight:800;color:var(--lime-text);line-height:1.1}
  .projects-rule{width:94px;height:3px;background:var(--lime-text);margin:6px 0 22px}
  .project-list{position:absolute;top:82px;color:var(--white)}
  .project-list li{height:34px;font-size:12.5px}
  .project-list.left{left:11px}
  .project-list.right{left:178px}

  .project-photo{position:absolute;border-radius:50%;border:5px solid var(--forest);box-shadow:0 0 0 3px rgba(255,255,255,.7) inset}
  .project-photo.street{left:38px;top:651px;width:226px;height:226px;background:linear-gradient(180deg,#9ab6d8 0%,#6e8a5c 35%,#b9bbb6 60%,#8c8e89 100%)}
  .project-photo.courtyard{left:278px;top:780px;width:220px;height:220px;background:linear-gradient(180deg,#e8e4da 0%,#5d9a45 30%,#4b5158 60%,#3b4047 100%)}
  .project-photo.screen{left:543px;top:778px;width:220px;height:220px;background:linear-gradient(160deg,#4f78b8 0%,#c8ad86 40%,#9a5a3a 75%,#5a3020 100%)}

  .back-brand{position:absolute;left:38px;top:924px;width:250px;text-align:center}
  .back-brand .brand-mark{width:132px;height:132px;margin-bottom:8px}
  .back-brand .brand-name{font-size:19px}

  .call{position:absolute;left:520px;top:1030px;border-left:4px solid var(--lime);padding-left:10px;color:var(--white)}
  .call-lead{font-size:24px;font-weight:700;line-height:1.1}
  .call-number{font-size:40px;font-weight:700;line-height:1.15}
</style>
</head>
<body>
<div class="sheet">

  <!-- Front side -->
  <section class="page page-front">
    <div class="hero-photo" role="img" aria-label="Photo of an excavator on a paving site at sunset"></div>
    <div class="greenery-photo" role="img" aria-label="Soft photo of fresh green leaves"></div>

    <svg class="waves" width="810" height="700" viewBox="0 0 810 700" aria-hidden="true">
      <path fill="#7cc242" d="M0,480 C40,432 110,412 180,418 C260,426 300,490 360,535 C420,578 520,585 620,552 C700,526 760,492 810,462 L810,528 C700,590 560,652 400,652 C250,652 120,610 0,572 Z"/>
      <path fill="#ffffff" d="M0,572 C120,610 250,652 400,652 C560,652 700,590 810,528 L810,548 C700,610 560,672 400,672 C250,672 120,630 0,592 Z"/>
      <path fill="#138a36" d="M0,536 C120,575 250,620 400,620 C560,620 700,558 810,496 L810,528 C700,590 560,652 400,652 C250,652 120,610 0,572 Z"/>
    </svg>

    <div class="brand">
      <div class="brand-mark"></div>
      <div class="brand-name">Brenmoss Building Company</div>
    </div>

    <header class="headline">
      <span class="headline-rule"></span>
      <div class="headline-line">RESIDENTIAL</div>
      <div class="headline-line">&amp; COMMERCIAL</div>
      <div class="headline-key">LANDSCAPING</div>
      <div class="headline-place"><b>BASED IN</b> <span>CANTERBURY</span></div>
    </header>

    <div class="experience">
      <div class="experience-lead">With more than</div>
      <div class="experience-years">25 YEARS</div>
      <div class="experience-tail">experience in the<br>landscaping industry</div>
    </div>

    <div class="work-photo timber" role="img" aria-label="Photo of timber decking boards"></div>
    <div class="work-photo lawn" role="img" aria-label="Photo of a lawn sprinkler beside a path"></div>
    <div class="work-photo paving" role="img" aria-label="Photo of concrete paving slabs"></div>

    <div class="services">
      <h2 class="services-title">SERVICES</h2>
      <div class="services-rule"></div>
      <p class="services-intro">As a full construction landscaping company, we formally offer the following services. However, we regularly work with clients who want something a little out of the box. If there is something in particular you are after, we are happy to discuss options with you.</p>
    </div>

    <ul class="tick-list service-list col-1">
      <li>Patios</li><li>Paving</li><li>Concrete</li><li>Water Features</li><li>Decking</li>
    </ul>
    <ul class="tick-list service-list col-2">
      <li>Fencing</li><li>Boardwalks</li><li>Timber</li><li>Planter Boxes</li><li>Pergolas</li>
    </ul>
    <ul class="tick-list service-list col-3">
      <li>Retaining Walls</li><li>Gardens &amp; Lawns</li><li>Irrigation</li><li>Project Management</li><li>Consultation</li>
    </ul>

    <footer class="contact-bar">
      <div class="contact-item">
        <svg width="18" height="18" viewBox="0 0 24 24"><path fill="#138a36" d="M6.6 10.8a15.1 15.1 0 006.6 6.6l2.2-2.2c.3-.3.7-.4 1-.2 1.1.4 2.3.6 3.6.6.6 0 1 .4 1 1V20c0 .6-.4 1-1 1A17 17 0 013 4c0-.6.4-1 1-1h3.5c.6 0 1 .4 1 1 0 1.3.2 2.5.6 3.6.1.3 0 .7-.2 1z"/></svg>
        021 555 0148
      </div>
      <div class="contact-item">
        <svg width="20" height="15" viewBox="0 0 20 15"><rect x="0.5" y="0.5" width="19" height="14" fill="#138a36"/><path d="M1 1l9 7 9-7" stroke="#abd037" stroke-width="1.6" fill="none"/></svg>
        hello@brenmossbc.co.nz
      </div>
      <div class="contact-item">
        <svg width="19" height="19" viewBox="0 0 20 20"><circle cx="10" cy="10" r="9" fill="#138a36"/><path d="M1 10h18M10 1c-4 4-4 14 0 18M10 1c4 4 4 14 0 18" stroke="#abd037" stroke-width="1.3" fill="none"/></svg>
        www.brenmossbc.co.nz
      </div>
    </footer>
  </section>

  <!-- Back side -->
  <section class="page page-back">
    <div class="back-photo" role="img" aria-label="Green-tinted photo of a hedge and lawn"></div>
    <div class="decking-photo" role="img" aria-label="Photo of weathered timber decking beside a lawn"></div>
    <div class="bench-photo" role="img" aria-label="Photo of a dark timber bench"></div>

    <svg class="swoosh" width="810" height="1146" viewBox="0 0 810 1146" aria-hidden="true">
      <path fill="#ffffff" d="M0,625 C150,770 300,885 450,893 C600,900 720,872 810,850 L810,858 C720,880 600,908 450,901 C300,893 150,778 0,633 Z"/>
      <path fill="#7cc242" d="M0,640 C150,785 300,900 450,908 C600,915 720,888 810,866 L810,892 C720,914 600,942 450,935 C300,928 150,830 0,700 Z"/>
    </svg>

    <div class="project-grid">
      <div class="grid-fence" role="img" aria-label="Photo of a timber slat fence"></div>
      <div class="grid-path" role="img" aria-label="Photo of a concrete path beside a lawn"></div>
      <div class="grid-bench" role="img" aria-label="Photo of a timber bench on a paved courtyard"></div>
      <div class="grid-pool" role="img" aria-label="Photo of pool-side paving"></div>
    </div>

    <div class="about">
      <h2 class="about-title">ABOUT US</h2>
      <p>With more than 25 years experience in the landscaping industry, Brenmoss Building Company offers services to large or small residential and commercial projects. Based in Canterbury, we are locally owned and operated. Whether you have a blank canvas or are looking to rejuvenate your property we are able to advise and make the process easy and stress free. From paving, pergolas and decks to concrete or planting your dream garden we have the expertise to help.</p>
      <p class="about-values">Our company is built on honesty, teamwork, sound knowledge and a determination to provide our customers with the highest quality product and service. We are a small team of highly skilled, dedicated and reliable professionals who complete projects efficiently and with outstanding workmanship.</p>
      <p>We hold Stonecrest Pro Accreditation status making us preferred installers of this paving system. To achieve this we had to show we had a solid understanding of the system and the skill set to ensure workmanship was held to the highest standard.</p>
      <p>How we work is simple. We will listen, get a clear idea of your vision and offer practical advice in order to achieve the best outcome within your budget and scope. An initial consultation is free so give us a call and let's chat about getting the best solution to your landscaping needs.</p>
    </div>

    <div class="projects">
      <h2 class="projects-title">OUR PROJECTS</h2>
      <div class="projects-rule"></div>
      <ul class="tick-list project-list left">
        <li>Streetscapes</li><li>Ashgrove</li><li>Newbury</li>
      </ul>
      <ul class="tick-list project-list right">
        <li>Maple Place</li><li>Rangiora Project</li><li>Elmwood Street &amp; More</li>
      </ul>
    </div>

    <div class="project-photo street" role="img" aria-label="Photo of a new paved streetscape"></div>
    <div class="project-photo courtyard" role="img" aria-label="Photo of a tiled courtyard with hedging"></div>
    <div class="project-photo screen" role="img" aria-label="Photo of a timber screen and bench"></div>

    <div class="brand back-brand">
      <div class="brand-mark"></div>
      <div class="brand-name">Brenmoss Building Company</div>
    </div>

    <div class="call">
      <div class="call-lead">Call Us Today!</div>
      <div class="call-number">021 555 0148</div>
    </div>
  </section>

</div>
</body>
</html>
```